Dental practice logo either "Pearlvale Oral Studio" or "Dental Lumora Centre"

Dental practice with either of the logos mentioned above as we haven't decided on the name depends on which one looks better. Our motto of the practice is to create beautiful smiles and perform general dentistry.
Dr Suresh Nandakumar
47 Wattlebrook Road
Deeragun
Queensland 4814 and also the contact number, email address and website.
On the backside of the card it should be about the next appointment and also mention on the bottom" If unable to keep an appointment kindly give 24 hours notice otherwise a fee will be charged for the time reserved.
Reason: As it may take longer to design
We want the business card only on the dental practice named Dental Lumora Centre and with a caption underneath the practice name as "Townsville's home of dentistry"
Target Market(s)
dental patients and general population who want beautiful smile
Industry/Entity Type
Dental

```html
<!DOCTYPE html>
<html lang="en">
<head>
<meta charset="UTF-8">
<title>Next Appointment Card</title>
<link rel="stylesheet" href="https://fonts.googleapis.com/css2?family=Arimo:wght@700&display=swap">
<style>
  :root {
    --card-green: #9cc93b;
    --tooth-light: #c3e07e;
    --tooth-mid: #b2d663;
    --text-white: #ffffff;
    --rule-black: #111111;
  }
  html, body {
    margin: 0;
    padding: 0;
    width: 1200px;
    height: 680px;
    overflow: hidden;
  }
  .card {
    position: relative;
    width: 1200px;
    height: 680px;
    background: var(--card-green);
    font-family: "Arimo", Arial, sans-serif;
    color: var(--text-white);
    overflow: hidden;
  }
  .card-title {
    position: absolute;
    top: 30px;
    left: 0;
    width: 100%;
    margin: 0;
    text-align: center;
    font-size: 78px;
    font-weight: 700;
    letter-spacing: -2px;
    word-spacing: 10px;
    line-height: 1.2;
  }
  .title-rule {
    position: absolute;
    top: 137px;
    left: 281px;
    width: 627px;
    height: 3px;
    background: var(--rule-black);
  }
  .tooth-art {
    position: absolute;
    top: 152px;
    left: 446px;
    width: 243px;
    height: 408px;
    border-radius: 42% 42% 30% 30%;
    background: radial-gradient(ellipse at 50% 35%, var(--tooth-light) 0%, var(--tooth-mid) 55%, rgba(178, 214, 99, 0) 100%);
    opacity: 0.85;
  }
  .cancellation-note {
    position: absolute;
    top: 596px;
    left: 0;
    width: 100%;
    margin: 0;
    text-align: center;
    font-size: 28px;
    font-weight: 700;
    letter-spacing: -1px;
    line-height: 40px;
  }
</style>
</head>
<body>
  <main class="card">
    <h1 class="card-title">Next Appointment</h1>
    <div class="title-rule"></div>
    <div class="tooth-art" role="img" aria-label="Faint illustration of a single molar tooth"></div>
    <p class="cancellation-note">“If unable to keep an appointment kindly give 24 hours notice<br>otherwise a fee will be charged for the time reserved”</p>
  </main>
</body>
</html>
```